VELVET RUMBA/New Packaging Design

We need a new packaging design for our product. We are looking a fresh image and something that catches attention from the consumer.

Velvet Rumba is a mix of selected dried peppers and sugar.

Our company name is Brelodan, we own the brand Vopri, we have offices in Mexico & United States. www.brelodan.example www.vopri.example

```html
<!DOCTYPE html>
<html lang="en">
<head>
<meta charset="utf-8">
<title>Vopri Velvet Rumba – Pouch Front</title>
<link href="https://fonts.googleapis.com/css2?family=Josefin+Sans:wght@300&family=Lilita+One&family=Montserrat:wght@400;600;700&display=swap" rel="stylesheet">
<style>
  :root {
    --backdrop: #ecebea;
    --pouch-white: #ffffff;
    --pouch-red: #e0262e;
    --pouch-red-dark: #c41d24;
    --brand-ink: #3a3a3a;
    --mark-green: #2e9a5b;
    --chili-red: #d8232b;
    --chili-light: #f0605f;
    --blend-dark: #7a5418;
    --blend-light: #b38a3a;
    --text-light: #ffffff;
    --text-soft: #fbe3e3;
  }
  * { margin: 0; padding: 0; box-sizing: border-box; }
  html, body {
    width: 1200px; height: 1000px; overflow: hidden;
    background: var(--backdrop);
  }
  .canvas {
    position: relative; width: 1200px; height: 1000px;
  }
  .pouch-front {
    position: absolute; left: 370px; top: 40px;
    width: 460px; height: 920px;
    background: var(--pouch-white);
    border-radius: 14px;
    overflow: hidden;
    box-shadow: 0 6px 24px rgba(0,0,0,0.12);
  }
  .brand-lockup {
    position: absolute; top: 150px; left: 0; width: 100%;
    display: flex; flex-direction: column; align-items: center; gap: 26px;
  }
  .brand-dot {
    width: 150px; height: 150px; border-radius: 50%;
    background: var(--mark-green);
  }
  .brand-name {
    font-family: "Josefin Sans", sans-serif; font-weight: 300;
    font-size: 64px; color: var(--brand-ink); line-height: 1;
  }
  .chili-art {
    position: absolute; top: 398px; left: 80px;
    width: 300px; height: 92px;
  }
  .flavour-band {
    position: absolute; top: 470px; left: 0; width: 100%; bottom: 0;
    background: var(--pouch-red);
    display: flex; flex-direction: column; align-items: center;
    color: var(--text-light);
  }
  .flavour-name {
    margin-top: 30px;
    font-family: "Lilita One", sans-serif;
    font-size: 60px; letter-spacing: 1px; line-height: 1;
    text-shadow: 2px 3px 0 rgba(90,10,10,0.55);
  }
  .divider {
    width: 400px; height: 1px; margin-top: 18px;
    background: var(--text-soft); opacity: 0.7;
  }
  .flavour-sub {
    margin-top: 36px;
    font-family: "Montserrat", sans-serif; font-weight: 600;
    font-size: 25px; letter-spacing: 2px;
  }
  .tagline {
    margin-top: 16px; text-align: center;
    font-family: "Montserrat", sans-serif; font-weight: 400;
    font-size: 13px; letter-spacing: 1.2px; line-height: 1.45;
    text-transform: uppercase; color: var(--text-soft);
  }
  .tagline strong { font-weight: 700; color: var(--text-light); }
  .product-window {
    margin-top: 4px; width: 400px; height: 88px;
    border-radius: 3px;
    background: linear-gradient(180deg, var(--blend-light), var(--blend-dark));
    border: 1px solid rgba(255,255,255,0.6);
  }
  .net-weight {
    margin-top: 28px;
    font-family: "Montserrat", sans-serif; font-weight: 400;
    font-size: 19px; letter-spacing: 1.5px;
  }
  .net-weight strong { font-weight: 700; }
</style>
</head>
<body>
  <main class="canvas">
    <section class="pouch-front">
      <div class="brand-lockup">
        <div class="brand-dot"></div>
        <div class="brand-name">Vopri</div>
      </div>

      <svg class="chili-art" viewBox="0 0 300 92" role="img" aria-label="Illustration of a red chili pepper with green stem and leaves">
        <defs>
          <linearGradient id="chiliTone" x1="0" y1="0" x2="0" y2="1">
            <stop offset="0" stop-color="#f0605f"/>
            <stop offset="1" stop-color="#c41d24"/>
          </linearGradient>
        </defs>
        <rect x="0" y="0" width="300" height="92" rx="46" fill="url(#chiliTone)"/>
      </svg>

      <div class="flavour-band">
        <h1 class="flavour-name">VELVET RUMBA</h1>
        <div class="divider"></div>
        <p class="flavour-sub">PICANTE</p>
        <p class="tagline">Heat up snack time<br>with the perfect blend<br>of <strong>spicy</strong> and <strong>sweet</strong></p>
        <div class="product-window" role="img" aria-label="Clear window showing the chili and sugar blend inside"></div>
        <p class="net-weight">NET WT <strong>5.3</strong> OZ.<strong>(150g)</strong></p>
      </div>
    </section>
  </main>
</body>
</html>
```